Social Media Template Design for a leading Veterinary Clinic in Austria

We are looking for social media design templates including the following:
- single picture posting (Moxiverse & QL)
- carousel postings (Moxiverse)
- story (Moxiverse & QL)
- reel thumbnail (Moxiverse & QL)
- story highlight design (Moxiverse)

What are the templates for?
We are working on a way to make posting content more efficient. Therefore, we'd like to use templates for a more efficient content creation in the future. In this way on the one hand, we expect creating different kind of content to be easier and faster, on the other it should create consistency throughout our channels.. We work with Adobe CC and mostly use Photoshop or Indesign for content creation.

How should they look?
The two strongest colors of our CI are dark blue and gold. We expect templates in which these colors are the unifying element. We think that our logo does not have to appear. Our brand identity is modern, clean, professional, revolutionary and yet inviting. Our social presence should also convey this impression. Our postings contain images and text. As an example for template use, we plan on introducing our employees - here we would have to use the employee's photo and insert title and name.

At the moment it is hard to tell how many designs we will need in total, as we might need to adapt or extend the template after the first use cases.
But for the start we'd aprox. expect:
- 2-3 different story slides
- 3 carousel slides
- 1 reel thumbnail
- 1 story highlight design, in which we can adapt the icons on our own

Do you think, you can help us out?

Already looking forward to your design ideas! 😊 Feel free to contact us for any further questions.

Target Market(s)

Austria

Industry/Entity Type

Veterinary Medicine

Font styles to use
Serif
Sans Serif

Colors

Designer to choose colors to be used in the design.

Requirements
Must have
• templates for Adobe Photoshop or InDesign in formats 1:1, 9:16, 4:5 according to content (story, posting, reel etc.) and channel
Should not have
• ready-to-post content, content ideas - only templates we can fill with content

```html
<!DOCTYPE html>
<html lang="de">
<head>
<meta charset="utf-8">
<title>Tiervita – Social Media Templates</title>
<link rel="stylesheet" href="https://fonts.googleapis.com/css2?family=Poppins:wght@400;500;700;800&display=swap">
<style>
  :root{
    --board:#8e9ad6;
    --navy:#2a3446;
    --navy-deep:#222b3b;
    --gold:#e2a31b;
    --white:#ffffff;
    --muted:#c9ced8;
  }
  *{box-sizing:border-box;margin:0;padding:0}
  html,body{width:1200px;height:3780px;overflow:hidden}
  body{background:var(--board);font-family:"Poppins",Arial,sans-serif;color:var(--white);position:relative}
  svg.defs{position:absolute;width:0;height:0}

  .post{position:absolute;width:840px;height:840px;background:var(--navy);overflow:hidden;box-shadow:0 18px 40px rgba(30,35,70,.35)}
  .post--welcome{left:180px;top:140px}
  .post--team{left:180px;top:1200px}
  .post--intro{left:180px;top:2260px}

  .preview-row{position:absolute;left:60px;top:3380px;width:1080px;height:340px}
  .preview{position:absolute;top:0;width:340px;height:340px;overflow:hidden;box-shadow:0 10px 24px rgba(30,35,70,.3)}
  .preview .post{left:0;top:0;transform:scale(.40476);transform-origin:0 0;box-shadow:none}
  .preview--1{left:0}.preview--2{left:370px}.preview--3{left:740px}

  .ring{position:absolute}
  .accent-bar{position:absolute;width:22px;height:100px;background:var(--white)}
  .brand{position:absolute;left:44px;top:36px;display:flex;align-items:center;gap:14px;font-weight:700;font-size:24px;color:var(--white)}
  .brand__dot{width:46px;height:46px;border-radius:50%;background:var(--gold)}

  .photo{position:absolute;background:linear-gradient(160deg,#8d939c,#4b5260 60%,#2f3644)}
  .headline{position:absolute;font-weight:800;font-size:62px;line-height:1.08;color:var(--white);letter-spacing:-.5px}
  .headline--team{left:462px;top:300px;width:330px;font-size:50px}
  .headline em{font-style:normal;color:var(--gold)}
  .body-copy{position:absolute;font-size:16px;line-height:1.55;color:var(--muted)}
  .tag{position:absolute;background:var(--gold);padding:12px 18px;color:var(--white)}
  .tag__title{font-weight:700;font-size:20px;line-height:1.2}
  .tag__sub{font-size:13px}
  .url,.phone{position:absolute;font-size:18px;font-weight:500;color:var(--white)}
  .phone{font-size:26px;font-weight:500}
  .paws{position:absolute;fill:var(--gold)}
  .hashtags{position:absolute;font-weight:800;font-size:32px;line-height:1.25;color:var(--white)}
  .hashtags span{color:var(--gold)}
</style>
</head>
<body>
<svg class="defs" aria-hidden="true">
  <symbol id="paw" viewBox="0 0 40 40">
    <ellipse cx="20" cy="27" rx="10" ry="8"/>
    <circle cx="8" cy="16" r="4"/><circle cx="15" cy="9" r="4"/>
    <circle cx="25" cy="9" r="4"/><circle cx="32" cy="16" r="4"/>
  </symbol>
</svg>

<!-- Post: Welcome (building) -->
<section class="post post--welcome">
  <svg class="ring" style="left:480px;top:-260px" width="520" height="520" viewBox="0 0 520 520" aria-hidden="true">
    <circle cx="260" cy="260" r="210" fill="none" stroke="var(--gold)" stroke-width="90"/>
  </svg>
  <div class="brand"><span class="brand__dot"></span>Tiervita</div>
  <div class="photo" role="img" aria-label="Clinic building with a basset hound in front" style="left:430px;top:110px;width:370px;height:610px;border-radius:300px 0 0 0"></div>
  <h1 class="headline" style="left:70px;top:250px;width:390px">Herzlich willkommen im <em>Tiervita</em>!</h1>
  <p class="body-copy" style="left:70px;top:545px;width:340px">Das Tiervita ist eine der größten und modernsten privaten Tierkliniken Europas direkt im Süden Wiens. Bei uns hat die beste tiermedizinische Versorgung Ihres Vierbeiners oberste Priorität.</p>
  <div class="tag" style="left:630px;top:570px;width:180px"><div class="tag__title">Tiervita</div><div class="tag__sub">für Tierbesitzer</div></div>
  <svg class="paws" style="left:690px;top:730px" width="110" height="60" aria-hidden="true"><use href="#paw" x="0" y="20" width="36" height="36"/><use href="#paw" x="40" y="0" width="30" height="30"/><use href="#paw" x="74" y="24" width="32" height="32"/></svg>
  <div class="url" style="left:600px;top:790px">www.tiervita.at</div>
</section>

<!-- Post: Team at work -->
<section class="post post--team">
  <svg class="ring" style="left:360px;top:-300px" width="640" height="640" viewBox="0 0 640 640" aria-hidden="true">
    <circle cx="320" cy="320" r="240" fill="none" stroke="var(--gold)" stroke-width="110"/>
  </svg>
  <div class="accent-bar" style="left:818px;top:300px"></div>
  <div class="brand"><span class="brand__dot"></span>Tiervita</div>
  <div class="photo" role="img" aria-label="Veterinary staff examining a dog" style="left:0;top:110px;width:440px;height:420px;border-radius:0 0 240px 0"></div>
  <div class="tag" style="left:0;top:440px;width:180px"><div class="tag__title">Tiervita</div><div class="tag__sub">für Tierbesitzer</div></div>
  <h1 class="headline headline--team">Herzlich willkommen im <em>Tiervita</em>!</h1>
  <p class="body-copy" style="left:462px;top:590px;width:330px">Das Tiervita ist eine der größten und modernsten privaten Tierkliniken Europas direkt im Süden Wiens. Bei uns hat die beste tiermedizinische Versorgung Ihres Vierbeiners oberste Priorität.</p>
  <svg class="paws" style="left:50px;top:600px" width="130" height="130" aria-hidden="true"><use href="#paw" x="0" y="0" width="38" height="38"/><use href="#paw" x="56" y="20" width="34" height="34"/><use href="#paw" x="14" y="64" width="36" height="36"/><use href="#paw" x="80" y="86" width="30" height="30"/></svg>
  <div class="url" style="left:180px;top:785px">www.tiervita.at</div>
  <div class="phone" style="left:530px;top:775px">+43(0)1 55501</div>
</section>

<!-- Post: Team introduction -->
<section class="post post--intro">
  <svg class="ring" style="left:-200px;top:380px" width="640" height="640" viewBox="0 0 640 640" aria-hidden="true">
    <circle cx="320" cy="320" r="230" fill="none" stroke="var(--gold)" stroke-width="110"/>
  </svg>
  <svg class="ring" style="left:620px;top:800px" width="260" height="130" viewBox="0 0 260 130" aria-hidden="true">
    <circle cx="130" cy="130" r="100" fill="none" stroke="var(--gold)" stroke-width="50"/>
  </svg>
  <div class="brand" style="left:auto;right:44px"><span class="brand__dot"></span>Tiervita</div>
  <div class="photo" role="img" aria-label="Black-and-white portrait of a smiling veterinarian" style="left:40px;top:120px;width:420px;height:720px;background:linear-gradient(180deg,#c9ccd1,#7d828b 55%,#3a404b)"></div>
  <div class="tag" style="left:0;top:700px;width:250px"><div class="tag__title" style="font-size:18px">Dr. Lena Maria Brunner</div><div class="tag__sub">der Notfallmedizin</div></div>
  <h1 class="headline" style="left:470px;top:150px;width:360px;font-size:56px">Dürfen Wir <em>Vorstellen?</em></h1>
  <p class="body-copy" style="left:470px;top:330px;width:330px">Ich bin in Graz geboren und aufgewachsen. Nach meinem Studium in Wien zog es mich für ein Praktikum in die Schweiz, bevor ich vor drei Jahren ins Tiervita kam.</p>
  <div class="hashtags" style="left:520px;top:520px"><span>#</span>Tiervita<br><span>#</span>Chirurgie</div>
  <div class="url" style="left:620px;top:680px;font-size:15px">www.tiervita.at</div>
  <div class="phone" style="left:570px;top:710px">+43(0)1 55501</div>
</section>

<!-- Overview row -->
<div class="preview-row">
  <div class="preview preview--1">
    <section class="post">
      <svg class="ring" style="left:360px;top:-300px" width="640" height="640" viewBox="0 0 640 640" aria-hidden="true"><circle cx="320" cy="320" r="240" fill="none" stroke="var(--gold)" stroke-width="110"/></svg>
      <div class="accent-bar" style="left:818px;top:300px"></div>
      <div class="brand"><span class="brand__dot"></span>Tiervita</div>
      <div class="photo" role="img" aria-label="Veterinary staff examining a dog" style="left:0;top:110px;width:440px;height:420px;border-radius:0 0 240px 0"></div>
      <div class="tag" style="left:0;top:440px;width:180px"><div class="tag__title">Tiervita</div><div class="tag__sub">für Tierbesitzer</div></div>
      <h1 class="headline headline--team">Herzlich willkommen im <em>Tiervita</em>!</h1>
      <svg class="paws" style="left:50px;top:600px" width="130" height="130" aria-hidden="true"><use href="#paw" x="0" y="0" width="38" height="38"/><use href="#paw" x="56" y="20" width="34" height="34"/><use href="#paw" x="14" y="64" width="36" height="36"/></svg>
      <div class="url" style="left:180px;top:785px">www.tiervita.at</div>
      <div class="phone" style="left:530px;top:775px">+43(0)1 55501</div>
    </section>
  </div>
  <div class="preview preview--2">
    <section class="post">
      <svg class="ring" style="left:-200px;top:380px" width="640" height="640" viewBox="0 0 640 640" aria-hidden="true"><circle cx="320" cy="320" r="230" fill="none" stroke="var(--gold)" stroke-width="110"/></svg>
      <div class="brand" style="left:auto;right:44px"><span class="brand__dot"></span>Tiervita</div>
      <div class="photo" role="img" aria-label="Black-and-white portrait of a smiling veterinarian" style="left:40px;top:120px;width:420px;height:720px;background:linear-gradient(180deg,#c9ccd1,#7d828b 55%,#3a404b)"></div>
      <div class="tag" style="left:0;top:700px;width:250px"><div class="tag__title" style="font-size:18px">Dr. Lena Maria Brunner</div><div class="tag__sub">der Notfallmedizin</div></div>
      <h1 class="headline" style="left:470px;top:150px;width:360px;font-size:56px">Dürfen Wir <em>Vorstellen?</em></h1>
      <div class="hashtags" style="left:520px;top:520px"><span>#</span>Tiervita<br><span>#</span>Chirurgie</div>
      <div class="phone" style="left:570px;top:710px">+43(0)1 55501</div>
    </section>
  </div>
  <div class="preview preview--3">
    <section class="post">
      <svg class="ring" style="left:480px;top:-260px" width="520" height="520" viewBox="0 0 520 520" aria-hidden="true"><circle cx="260" cy="260" r="210" fill="none" stroke="var(--gold)" stroke-width="90"/></svg>
      <div class="brand"><span class="brand__dot"></span>Tiervita</div>
      <div class="photo" role="img" aria-label="Clinic building with a basset hound in front" style="left:430px;top:110px;width:370px;height:610px;border-radius:300px 0 0 0"></div>
      <h1 class="headline" style="left:70px;top:250px;width:390px">Herzlich willkommen im <em>Tiervita</em>!</h1>
      <div class="tag" style="left:630px;top:570px;width:180px"><div class="tag__title">Tiervita</div><div class="tag__sub">für Tierbesitzer</div></div>
      <div class="url" style="left:600px;top:790px">www.tiervita.at</div>
    </section>
  </div>
</div>
</body>
</html>
```